Security Warning Sign

We have an existing sign that needs an update. I have attached a picture of the current square sign. We need to maintain the same wording. It needs to be professional and appropriate to attach to our customers fence. Also attached is a copy of our building sign which may lend some inspiration and hopefully the ai format will assist. The final sign will be 600mm x 600mmOur website is www.halvorngate.com.au

```html
<!DOCTYPE html>
<html lang="en">
<head>
<meta charset="utf-8">
<title>Security Warning Sign – Halvorngate Security</title>
<link rel="stylesheet" href="https://fonts.googleapis.com/css2?family=Montserrat:wght@700;800&family=Roboto+Condensed:wght@600;700&family=Open+Sans:wght@600;700&display=swap">
<style>
  :root {
    --frame: #222220;
    --orange: #f26b25;
    --white: #ffffff;
    --ink: #222220;
  }
  html, body {
    margin: 0;
    padding: 0;
    width: 1200px;
    height: 1200px;
    overflow: hidden;
    background: var(--white);
  }
  h1, p { margin: 0; }
  .sign {
    position: relative;
    width: 1200px;
    height: 1200px;
    background: var(--frame);
    overflow: hidden;
  }
  .top-strip {
    position: absolute;
    left: 20px;
    top: 28px;
    width: 1157px;
    height: 45px;
    background: var(--orange);
  }
  .headline {
    position: absolute;
    left: 0;
    top: 73px;
    width: 1200px;
    height: 202px;
    display: flex;
    align-items: center;
    justify-content: center;
    gap: 24px;
  }
  .headline-icon {
    width: 156px;
    height: 128px;
    flex: none;
  }
  .headline-text {
    font-family: "Montserrat", sans-serif;
    font-weight: 800;
    font-size: 162px;
    line-height: 1;
    color: var(--white);
    letter-spacing: -3px;
    margin-top: 4px;
  }
  .notice-panel {
    position: absolute;
    left: 20px;
    top: 275px;
    width: 1157px;
    height: 711px;
    background: var(--orange);
  }
  .camera-graphic {
    position: absolute;
    left: 0;
    top: 20px;
    width: 255px;
    height: 170px;
    background: linear-gradient(160deg, #2a2622 0%, #3a2c22 100%);
    border-radius: 0 40px 60px 0;
  }
  .notice-text {
    position: absolute;
    left: 0;
    top: 60px;
    width: 1157px;
    text-align: center;
    font-family: "Montserrat", sans-serif;
    font-weight: 700;
    font-size: 88px;
    line-height: 116px;
    color: var(--white);
    letter-spacing: 1px;
    padding-left: 10px;
    box-sizing: border-box;
  }
  .contact-band {
    position: absolute;
    left: 20px;
    top: 993px;
    width: 1157px;
    height: 184px;
    background: var(--white);
  }
  .brand {
    position: absolute;
    left: 70px;
    top: 38px;
    display: flex;
    align-items: center;
    gap: 18px;
  }
  .brand-dot {
    width: 92px;
    height: 92px;
    border-radius: 50%;
    background: var(--orange);
  }
  .brand-name {
    font-family: "Roboto Condensed", sans-serif;
    font-weight: 700;
    font-size: 112px;
    line-height: 1;
    color: var(--ink);
  }
  .company {
    position: absolute;
    left: 500px;
    top: 28px;
    text-align: left;
  }
  .company-name {
    font-family: "Roboto Condensed", sans-serif;
    font-weight: 600;
    font-size: 56px;
    line-height: 1;
    color: var(--orange);
  }
  .company-phone {
    font-family: "Open Sans", sans-serif;
    font-weight: 700;
    font-size: 86px;
    line-height: 1;
    color: var(--ink);
    margin-top: 10px;
    margin-left: -4px;
    letter-spacing: 1px;
  }
</style>
</head>
<body>
  <main class="sign">
    <div class="top-strip"></div>

    <header class="headline">
      <svg class="headline-icon" viewBox="0 0 156 128" aria-hidden="true">
        <path d="M78 6 L150 120 Q152 124 147 124 L9 124 Q4 124 6 120 Z" fill="var(--white)" stroke="var(--white)" stroke-width="8" stroke-linejoin="round"/>
        <rect x="71" y="40" width="14" height="48" rx="5" fill="var(--frame)"/>
        <circle cx="78" cy="104" r="8" fill="var(--frame)"/>
      </svg>
      <h1 class="headline-text">WARNING</h1>
    </header>

    <section class="notice-panel">
      <div class="camera-graphic" role="img" aria-label="Dark security camera on a wall bracket"></div>
      <p class="notice-text">ELECTRONIC<br>SURVEILLANCE<br>AND RECORDING<br>DEVICES INSTALLED<br>IN THIS AREA</p>
    </section>

    <footer class="contact-band">
      <div class="brand">
        <span class="brand-dot"></span>
        <span class="brand-name">HGS</span>
      </div>
      <div class="company">
        <p class="company-name">HALVORNGATE SECURITY</p>
        <p class="company-phone">1300 555 018</p>
      </div>
    </footer>
  </main>
</body>
</html>
```